"Cork Hollow Excursions" is a top notch Santa Barbara County Wine Tour company.

We provide scenic, boutique and custom wine tours. I need the card to be clean and classy. I will provide our logo. I would like the logo to cover the back side of the card as an option and would like to see a couple color options other then our signature green and gold. I would like to see some creative options and let the designers come up with options.
I need cards for myself and my team. The final design should communicate "An authentic and boutique wine tour experience"
Please use my website for reference www.corkhollowexcursions.com

Target Market(s)

We have a wide range of clients from millennials to baby boomers

Industry/Entity Type

Tour

Contact Information for Business Card

Contact info:
Dale Munford
805-291-6384
info@corkhollowexcursions.com
corkhollowexcursions.com

Colors

Designer to choose colors to be used in the design.

Requirements
Must have
• my logo
Nice to have
• *I would like to have the backside side with the logo and the company statement
• "An authentic and boutique wine tour experience" as an option.
• *I would also like to see what the designers can create!
• *I would like to see an option that incorporates or social: snapgrid, rovia, route scout
Should not have
• I do not want it too busy.

```html
<!DOCTYPE html>
<html lang="en">
<head>
<meta charset="utf-8">
<title>Cork Hollow Excursions – Business Card</title>
<link href="https://fonts.googleapis.com/css2?family=Open+Sans:wght@400;700&display=swap" rel="stylesheet">
<style>
  :root {
    --stage: #e9e9e9;
    --paper: #ffffff;
    --forest: #27694a;
    --forest-dark: #1f5a3e;
    --ink: #3d3d3d;
    --muted: #777777;
    --gold: #b59a7a;
  }
  * { box-sizing: border-box; margin: 0; padding: 0; }
  html, body { width: 1200px; height: 900px; overflow: hidden; }
  body {
    background: var(--stage);
    font-family: "Open Sans", sans-serif;
    display: flex;
    align-items: center;
    justify-content: center;
    gap: 90px;
  }
  .card {
    width: 340px;
    height: 595px;
    border-radius: 16px;
    position: relative;
    box-shadow: 0 3px 10px rgba(0,0,0,0.14);
  }
  .card-front { background: var(--paper); padding: 44px 36px 0 36px; }
  .card-back { background: var(--forest); color: #fff; }

  .holder-name { color: var(--forest); font-weight: 700; font-size: 30px; letter-spacing: 1px; line-height: 1.1; }
  .holder-title { color: var(--muted); font-size: 15px; margin-top: 2px; }

  .contact-list { list-style: none; margin-top: 34px; }
  .contact-list li {
    display: flex; align-items: flex-start; gap: 10px;
    font-size: 13.5px; color: var(--ink); line-height: 1.3; margin-bottom: 9px;
  }
  .contact-list svg { flex: 0 0 14px; width: 14px; height: 14px; margin-top: 2px; fill: var(--forest); }
  .social-dot { flex: 0 0 12px; width: 12px; height: 12px; border-radius: 50%; background: var(--forest); margin: 3px 1px 0 1px; }

  .brand-front {
    position: absolute; left: 36px; right: 36px; bottom: 70px; text-align: center;
  }
  .brand-mark-area {
    width: 170px; height: 100px; margin: 0 auto 18px;
    border-radius: 6px;
    background: linear-gradient(160deg, #3f8a63, var(--forest-dark));
  }
  .brand-name { font-weight: 700; font-size: 22px; letter-spacing: 2px; color: var(--gold); text-transform: uppercase; line-height: 1.25; }
  .brand-rule { height: 1px; background: var(--gold); width: 80%; margin: 12px auto 0; opacity: .7; }

  .brand-back {
    position: absolute; left: 30px; right: 30px; top: 170px; text-align: center;
  }
  .brand-back .brand-mark-area { background: linear-gradient(160deg, rgba(255,255,255,.9), rgba(255,255,255,.6)); }
  .brand-back .brand-name { color: #fff; font-size: 26px; }
  .brand-back .brand-rule { background: #fff; opacity: .6; }

  .social-row {
    position: absolute; left: 0; right: 0; bottom: 56px;
    display: flex; align-items: center; justify-content: center; gap: 10px;
    font-size: 11.5px; letter-spacing: .5px;
  }
  .social-row .line { width: 26px; height: 1px; background: #fff; opacity: .8; }
</style>
</head>
<body>

  <section class="card card-front" aria-label="Business card front">
    <h1 class="holder-name">Dale Munford</h1>
    <p class="holder-title">Title</p>

    <ul class="contact-list">
      <li><svg viewBox="0 0 16 16"><path d="M8 0a8 8 0 100 16A8 8 0 008 0zm0 1.5a6.5 6.5 0 110 13 6.5 6.5 0 010-13zM5.6 4l1.3 1.6-.7 1c.5 1.1 1.3 1.9 2.4 2.4l1-.7L11.2 9.6 10 11C7 10.5 5 8.5 4.6 5.5z"/></svg>805-291-6384</li>
      <li><svg viewBox="0 0 16 16"><path d="M1 3h14v10H1zM2 4.2V12h12V4.2L8 8.6z M2.8 4L8 7.7 13.2 4z"/></svg>info@corkhollowexcursions.com</li>
      <li><svg viewBox="0 0 16 16"><path d="M8 0a8 8 0 100 16A8 8 0 008 0zm-1 1.6v2.1L5 5.5 3 5A6.5 6.5 0 017 1.6zM8.5 14.4V12l2-2 2.7.9a6.5 6.5 0 01-4.7 3.5z"/></svg>www.corkhollowexcursions.com</li>
      <li><svg viewBox="0 0 16 16"><path d="M8 0a5.5 5.5 0 00-5.5 5.5C2.5 9.6 8 16 8 16s5.5-6.4 5.5-10.5A5.5 5.5 0 008 0zm0 3.2a2.3 2.3 0 110 4.6 2.3 2.3 0 010-4.6z"/></svg>228 Calle Vista Roble<br>Santa Barbara, CA 93101</li>
      <li><span class="social-dot"></span>www.snapgrid.com/CorkHollowTours</li>
      <li><span class="social-dot"></span>www.rovia.com/CorkHollowTours</li>
    </ul>

    <div class="brand-front">
      <div class="brand-mark-area" role="img" aria-label="Company emblem area: sun rising over vineyard rows and hills"></div>
      <p class="brand-name">Cork Hollow Excursions</p>
      <div class="brand-rule"></div>
    </div>
  </section>

  <section class="card card-back" aria-label="Business card back">
    <div class="brand-back">
      <div class="brand-mark-area" role="img" aria-label="Company emblem area: sun rising over vineyard rows and hills"></div>
      <p class="brand-name">Cork Hollow Excursions</p>
      <div class="brand-rule"></div>
    </div>

    <div class="social-row">
      <span class="line"></span>
      <span>friendhub</span>
      <span>snapgrid</span>
      <span>rovia</span>
      <span>route scout</span>
      <span class="line"></span>
    </div>
  </section>

</body>
</html>
```